Merchandising für ein Abbruch und Schadstoffsanierungsfirma
Zielgruppe
Wir sind ein Abbruch und Schadstoffsanierungsfirma aus Kassel.
Wir suchen hochwertige Design für Zollstöcke und a4 Blöcke.
Aufgabenstellung
Unser Logo und Daten sollten enthalten sein

```html
<!DOCTYPE html>
<html lang="de">
<head>
<meta charset="utf-8">
<title>Brandt Haus und Bauservice – Merchandising</title>
<link href="https://fonts.googleapis.com/css2?family=Josefin+Sans:wght@300;400;600&display=swap" rel="stylesheet">
<style>
  :root {
    --red: #dc2c2e;
    --red-dark: #a8282b;
    --navy: #1c1b2e;
    --black: #121212;
    --paper: #ffffff;
    --label-grey: #d4d4d4;
    --frame: #c8c8c8;
  }
  * { margin: 0; padding: 0; box-sizing: border-box; }
  html, body { width: 818px; height: 1200px; overflow: hidden; background: #fff; }
  body { font-family: "Josefin Sans", sans-serif; }
  .sheet { position: relative; width: 818px; height: 1200px; border: 1px solid var(--frame); overflow: hidden; }

  .version-label { position: absolute; top: 26px; font: 600 12px "Josefin Sans", sans-serif; color: var(--label-grey); }
  .notepad { position: absolute; top: 53px; width: 341px; height: 482px; background: var(--paper);
             box-shadow: 4px 5px 9px rgba(0,0,0,.28); }
  .notepad--v1 { left: 39px; }
  .notepad--v2 { left: 442px; }
  .notepad__band { position: absolute; left: 0; top: 0; width: 341px; background: var(--red);
                   border-bottom: 5px solid var(--red-dark); }
  .notepad--v1 .notepad__band { height: 38px; }
  .notepad--v2 .notepad__band { height: 46px; }
  .notepad__url { position: absolute; right: 27px; top: 17px; font-size: 6.5px; letter-spacing: .8px; color: #fff; }
  .notepad__grid { position: absolute; left: 28px; right: 28px; top: 55px; bottom: 52px;
    background-image: radial-gradient(circle, #b5b5b5 0.55px, transparent 0.8px);
    background-size: 7.5px 7.5px; }
  .notepad--v2 .notepad__grid { top: 59px; bottom: 28px; }

  .brand-name { text-align: center; color: var(--navy); line-height: 1; }
  .brand-name__main { font-weight: 600; letter-spacing: 1px; }
  .brand-name__sub { font-weight: 600; letter-spacing: .3px; }
  .notepad__brand { position: absolute; left: 0; right: 0; bottom: 12px; }
  .notepad__brand .brand-name__main { font-size: 15px; }
  .notepad__brand .brand-name__sub { font-size: 4.5px; margin-top: 3px; }
  .notepad__seal { position: absolute; right: 14px; top: -1px; width: 80px; height: 50px; background: #fff;
    border-radius: 0 0 40px 40px; display: flex; flex-direction: column; justify-content: center; }
  .notepad__seal .brand-name__main { font-size: 12px; }
  .notepad__seal .brand-name__sub { font-size: 4px; margin-top: 3px; }
  .notepad__footer { position: absolute; right: 28px; bottom: 11px; font-size: 5px; color: var(--red); letter-spacing: .2px; }
  .notepad__footer span + span::before { content: "|"; margin: 0 4px; }

  .ruler { position: absolute; left: 178px; width: 505px; }
  .ruler--front { top: 650px; height: 96px; background:
      repeating-linear-gradient(to bottom, transparent 0 10px, rgba(0,0,0,.25) 10px 11px), var(--red); }
  .ruler__scale { position: absolute; left: 0; top: 0; width: 100%; height: 13px; background: var(--black);
    display: flex; justify-content: space-between; padding: 2px 8px 0; color: #eee; font-size: 7px; }
  .ruler__services { position: absolute; left: 60px; top: 22px; list-style: none; color: #fff;
    font-variant: small-caps; font-size: 13px; line-height: 14px; letter-spacing: .3px; }
  .ruler__services li::before { content: "· "; }
  .ruler__brand-end { position: absolute; right: 0; top: 13px; bottom: 0; width: 150px;
    background: repeating-linear-gradient(to bottom, #eaeaea 0 10px, #9a9a9a 10px 11px);
    border-radius: 60px 0 0 60px / 41px 0 0 41px; display: flex; flex-direction: column; justify-content: center; }
  .ruler__brand-end .brand-name__main { font-size: 22px; }
  .ruler__brand-end .brand-name__sub { font-size: 7px; margin-top: 4px; }

  .ruler--back { top: 1030px; height: 78px; background:
      repeating-linear-gradient(to bottom, var(--black) 0 8px, #555 8px 9px); }
  .ruler__slogan { position: absolute; left: 0; right: 0; top: 16px; text-align: center; color: var(--red);
    font-variant: small-caps; font-size: 27px; font-weight: 400; line-height: 1; }
  .ruler__contact { position: absolute; left: 0; right: 0; top: 47px; text-align: center; color: #fff; font-size: 11px; }
</style>
</head>
<body>
<main class="sheet">
  <span class="version-label" style="left:40px">V1</span>
  <span class="version-label" style="left:443px">V2</span>

  <section class="notepad notepad--v1">
    <div class="notepad__band"></div>
    <span class="notepad__url">WWW.BRANDT-BAU-KASSEL.DE</span>
    <div class="notepad__grid"></div>
    <div class="notepad__brand brand-name">
      <div class="brand-name__main">BRANDT</div>
      <div class="brand-name__sub">HAUS UND BAUSERVICE</div>
    </div>
  </section>

  <section class="notepad notepad--v2">
    <div class="notepad__band"></div>
    <div class="notepad__seal brand-name">
      <div class="brand-name__main">BRANDT</div>
      <div class="brand-name__sub">HAUS UND BAUSERVICE</div>
    </div>
    <div class="notepad__grid"></div>
    <div class="notepad__footer"><span>WWW.BRANDT-BAU-KASSEL.DE</span><span>KONTAKT@BRANDT-BAU-KASSEL.DE</span><span>0151/228 40 17</span></div>
  </section>

  <section class="ruler ruler--front">
    <div class="ruler__scale"><span>1</span><span>2</span><span>3</span><span>4</span><span>5</span><span>6</span><span>7</span><span>8</span><span>9</span><span>10</span><span>11</span><span>12</span><span>13</span><span>14</span><span>15</span><span>16</span><span>17</span><span>18</span><span>19</span><span>20</span></div>
    <ul class="ruler__services">
      <li>Schadstoffsanierung</li>
      <li>Abbruch - Rückbau aller Gewerke</li>
      <li>Entkernung/Entrümplung</li>
      <li>Entsorgung/Verschrottung</li>
      <li>Kernbohrungen und vieles mehr!</li>
    </ul>
    <div class="ruler__brand-end brand-name">
      <div class="brand-name__main">BRANDT</div>
      <div class="brand-name__sub">HAUS UND BAUSERVICE</div>
    </div>
  </section>

  <section class="ruler ruler--back">
    <p class="ruler__slogan">Wenn Qualität entscheidet!</p>
    <p class="ruler__contact">WWW.BRANDT-BAU-KASSEL.DE - 0151/228 40 17</p>
  </section>
</main>
</body>
</html>
```